"A Touch RMB" Business Card/Logo Design

I'm looking for a very creative look for my new business called "A Touch RMB" on a business card design. Don't be distracted by my "business card details" below....if you have other ideas on how you see "A Touch RMB" go for it. If probably should somehow give a look that I paint furniture....maybe a paint drip or something simple or you can get more creative....sky's the limit and I really need your creative eye on how to per tray that "A Touch RMB" means taking something old and turning into new again with some paint.

Industry/Entity Type

Business

Contact Information for Business Card

I refurbish and up-cycle furniture that needs "a little TLC'....thus, my business name was born called "A Touch RMB" (Those are my initials). I mainly paint old furniture of all styles and bring them back to life. I sometimes recreate furniture as well....I will make benches from old headboards of all sizes, etc. I'd love to see design that incorporate the crafty/creative side of me. If that means incorporating a paint brush, tools, paint cans, or furniture such as dressers, old vintage furniture, spindles, etc, etc. I don't know if something creative could be done with my initials (RMB). I really have a creative block of ideas and need your help bringing my "A Touch RMB" business to life.

P.S. Below is just one picture that I thought was neat and creative as they used a paintbrush but used spindles for the bristles and put their logo in the middle. Just an idea I thought was very unique and creative.

I'm very excited to see your design. Thank you for taking the time to create my logo/business card for me.

Carla

Requirements
Must have
• Please include this information on the card:
• My Name: Carla Brennick
• Address: 14706 318th Ln SE, Fox Hollow, MN 55418
• E-Mail: atouchrmb@mailcove.net
• FB: http:/www.friendpage.net/atouchrmb
• Cell: 763-419-7082

```html
<!DOCTYPE html>
<html lang="en">
<head>
<meta charset="utf-8">
<title>A Touch RMB — Business Card</title>
<link rel="stylesheet" href="https://fonts.googleapis.com/css2?family=Montserrat:wght@400;500;700;800&display=swap">
<style>
  :root {
    --backdrop: #e9e6e2;
    --card-light: #ffffff;
    --card-dark: #050505;
    --brand-red: #b51f2e;
    --tag-red: #e23b4a;
    --ink: #2e2e30;
    --ink-soft: #1f1f1f;
    --paper-white: #ffffff;
    --ghost: rgba(181, 31, 46, 0.07);
  }
  * { margin: 0; padding: 0; box-sizing: border-box; }
  html, body {
    width: 1200px; height: 1000px; overflow: hidden;
    background: var(--backdrop);
    font-family: "Montserrat", Arial, sans-serif;
  }
  .card {
    position: absolute; left: 265px; width: 665px; height: 397px;
    box-shadow: 0 3px 10px rgba(0,0,0,0.25);
  }
  .card-front { top: 73px; background: var(--card-light); }
  .card-back { top: 532px; background: var(--card-dark); }

  .brand { position: absolute; display: flex; align-items: center; gap: 22px; }
  .brand-mark { background: var(--brand-red); flex: none; }
  .brand-name { font-weight: 800; line-height: 1.02; }
  .brand-name span { display: block; }
  .brand-name .line-lead { font-size: 38px; }
  .brand-name .line-initials { font-size: 54px; letter-spacing: 1px; }

  .card-front .brand { left: 32px; top: 50px; }
  .card-front .brand-mark { width: 118px; height: 118px; }
  .card-front .brand-name { color: var(--ink); }

  .card-back .brand { left: 125px; top: 118px; gap: 30px; }
  .card-back .brand-mark { width: 150px; height: 150px; }
  .card-back .brand-name { color: var(--paper-white); }
  .card-back .line-lead { font-size: 46px; }
  .card-back .line-initials { font-size: 68px; }

  .ghost-mark {
    position: absolute; left: 415px; top: 117px; width: 205px; height: 250px;
    background: var(--ghost);
  }

  .holder-name {
    position: absolute; left: 33px; top: 220px;
    color: var(--brand-red); font-weight: 700; font-size: 24px;
  }
  .contact-list { position: absolute; left: 33px; top: 262px; list-style: none; }
  .contact-list li {
    display: flex; align-items: center; gap: 6px;
    height: 28px; font-size: 17px; color: var(--ink-soft);
  }
  .contact-icon {
    width: 17px; height: 17px; background: var(--brand-red); border-radius: 2px;
    display: flex; align-items: center; justify-content: center; flex: none;
    color: var(--paper-white); font-size: 12px; font-weight: 700;
  }
  .address {
    position: absolute; left: 33px; top: 350px;
    font-size: 17px; color: var(--ink-soft);
  }
  .tagline {
    position: absolute; left: 0; right: 0; top: 347px; text-align: center;
    color: var(--tag-red); font-size: 17px; font-weight: 500;
  }
</style>
</head>
<body>
  <section class="card card-front">
    <div class="brand">
      <span class="brand-mark"></span>
      <p class="brand-name"><span class="line-lead">A Touch</span><span class="line-initials">RMB</span></p>
    </div>
    <div class="ghost-mark" role="img" aria-label="Faint brand mark decoration"></div>
    <h1 class="holder-name">Carla Brennick</h1>
    <ul class="contact-list">
      <li><span class="contact-icon"></span>atouchrmb</li>
      <li>
        <span class="contact-icon">
          <svg width="11" height="11" viewBox="0 0 24 24" aria-hidden="true"><path fill="#fff" d="M6.6 10.8a15.1 15.1 0 0 0 6.6 6.6l2.2-2.2c.3-.3.7-.4 1-.2 1.1.4 2.3.6 3.6.6.6 0 1 .4 1 1V20c0 .6-.4 1-1 1A17 17 0 0 1 3 4c0-.6.4-1 1-1h3.5c.6 0 1 .4 1 1 0 1.3.2 2.5.6 3.6.1.3 0 .7-.2 1z"/></svg>
        </span>763-419-7082
      </li>
      <li><span class="contact-icon">@</span>atouchrmb@mailcove.net</li>
    </ul>
    <p class="address">14706 318th Ln SE, Fox Hollow, MN 55418</p>
  </section>

  <section class="card card-back">
    <div class="brand">
      <span class="brand-mark"></span>
      <p class="brand-name"><span class="line-lead">A Touch</span><span class="line-initials">RMB</span></p>
    </div>
    <p class="tagline">Old pieces, fresh new color !</p>
  </section>
</body>
</html>
```